farvinta labs cybersecurity website design and development

website design and development for a cybersecurity company. we have a logo and would like site to suit logo colors and look
cybersecurity website should be secure and look professional
main example of site we want to use: https://www.plomvex.example/
site should be usable on tablet and phones

For each design proposal, please could you provide details of what language you'll use to code the website.

Target Market(s)

insurance companies, financial institutions, private SME, Africa and Europe

Coding

Coded - Design and coding required

Number of Pages Required

5+ page

Requirements
Must have
• 9 Pages:
Home
About us
Contacts
Partners
Blog
Services
( consulting, vulnerability assessment, information systems security audit, ISO compliance, Penetration testing, security awareness training, social engineering test, protection against DDoS, procurement )
Resources
Technologies
Careers
Nice to have
• nice to have all services have their own pages.
design based on logo colors and look

please provide what will be use to code the website

```html
<!DOCTYPE html>
<html lang="en">
<head>
<meta charset="utf-8">
<title>Farvinta Labs — Cybersecurity</title>
<link rel="stylesheet" href="https://fonts.googleapis.com/css2?family=Barlow:wght@400;500;600&display=swap">
<style>
:root{
  --navy:#1e2f86;
  --blue:#1779d3;
  --blue-deep:#1c4aa8;
  --sky:#2d9be6;
  --ink:#1c2340;
  --text:#555b6e;
  --line:#eceef4;
  --white:#ffffff;
}
*{box-sizing:border-box;margin:0;padding:0}
html,body{width:1200px;height:4454px;overflow:hidden;background:var(--white)}
body{position:relative;font-family:"Barlow",sans-serif;color:var(--ink)}
h1,h2,h3{font-weight:400}
.abs{position:absolute}
a{color:inherit;text-decoration:none}
.btn{position:absolute;display:flex;align-items:center;justify-content:center;border-radius:20px;font-size:12px;font-weight:500;letter-spacing:.4px;text-transform:uppercase}
.btn-navy{background:var(--navy);color:var(--white)}
.btn-blue{background:var(--blue);color:var(--white)}
.btn-white{background:var(--white);color:var(--blue-deep)}

/* header */
.topbar{top:12px;right:88px;font-size:13px;display:flex;gap:22px}
.topbar .mail{color:var(--blue)}
.topbar .call{color:var(--navy);font-weight:600}
.brand{left:87px;top:40px;display:flex;align-items:center;gap:10px}
.brand-dot{width:38px;height:38px;border-radius:50%;background:var(--navy)}
.brand-name{font-size:26px;font-weight:600;color:var(--navy)}
.nav{left:368px;top:74px;display:flex;gap:26px;font-size:13px;color:var(--ink)}
.nav .active{color:var(--blue)}
.nav-cta{left:990px;top:66px;width:122px;height:34px}

/* hero */
.hero{left:87px;top:123px;width:1113px;height:655px;border-radius:22px 0 0 150px;
  background:linear-gradient(120deg,#2b3f93 0%,#4f74b9 50%,#8fa9d8 100%)}
.hero-title{left:263px;top:350px;font-size:60px;line-height:62px;color:var(--white)}
.hero-cta{left:263px;top:506px;width:122px;height:32px}

/* services */
.sect-title{left:0;width:1200px;text-align:center;font-size:40px;line-height:50px;color:var(--navy)}
.services{left:87px;top:985px;width:1025px;display:grid;grid-template-columns:repeat(3,1fr);row-gap:17px}
.svc{height:190px;display:flex;flex-direction:column;align-items:center;justify-content:center;gap:18px;
  border-right:1px solid var(--line);border-bottom:1px solid var(--line);font-size:17px;font-weight:500;text-align:center;line-height:22px}
.svc:nth-child(3n){border-right:none}
.svc:nth-child(n+7){border-bottom:none}
.svc-icon{width:70px;height:70px;border-radius:14px;background:#e4ecfa}
.svc.featured{background:linear-gradient(180deg,var(--blue-deep),var(--sky));color:var(--white);border-radius:3px}
.svc.featured .svc-icon{background:rgba(255,255,255,.25)}
.rule{height:1px;background:var(--line)}

/* about */
.about-title{left:263px;top:1722px;font-size:40px;line-height:51px;color:var(--navy)}
.about-bar{left:149px;top:2101px;width:200px;height:290px;background:var(--blue)}
.about-photo{left:175px;top:1866px;width:411px;height:498px;border-radius:0 44px 0 0;
  background:linear-gradient(140deg,#3b3f47,#8d96a6 60%,#c7ccd6)}
.about-kicker{left:700px;top:1913px;font-size:16px;color:var(--blue)}
.about-lead{left:700px;top:1966px;width:330px;font-size:18px;line-height:29px;color:var(--blue-deep)}
.about-body{left:700px;top:2129px;width:330px;font-size:13px;line-height:21px;color:var(--text)}
.about-cta{left:700px;top:2281px;width:106px;height:32px}

/* cta band */
.band{left:0;top:2478px;width:1037px;height:306px;border-radius:0 130px 130px 0;
  background:linear-gradient(100deg,#2e68c2,#1a6fd0 60%,#2d8fe3)}
.band-title{left:178px;top:2528px;font-size:46px;line-height:62px;font-weight:500;color:var(--white)}
.band-cta{left:178px;top:2685px;width:158px;height:34px}

/* testimonials */
.client-photo{left:277px;top:2961px;width:224px;height:224px;border-radius:50%;border:4px solid var(--navy);
  background:linear-gradient(160deg,#d9dde6,#8a93a8)}
.quote-mark{left:588px;top:2960px;font-size:56px;line-height:40px;color:var(--blue);font-weight:600;letter-spacing:-4px}
.quote{left:588px;top:3014px;width:340px;font-size:13.5px;line-height:24.5px;color:var(--text)}
.quote-by{left:588px;top:3152px;font-size:13px;line-height:20px;color:var(--blue)}
.quote-by b{color:var(--navy);font-weight:500}
.dots{left:550px;top:3244px;display:flex;gap:9px}
.dots span{width:13px;height:13px;border-radius:50%;border:1.5px solid var(--blue)}
.dots span.on{background:var(--blue)}

/* articles */
.articles-title{left:263px;top:3394px;font-size:40px;line-height:50px;color:var(--navy)}
.articles-cta{left:832px;top:3403px;width:104px;height:34px}
.card{position:absolute;top:3505px;width:263px;height:437px;border:1px solid var(--line);border-radius:0 0 40px 0;background:var(--white)}
.card-img{width:263px;height:299px;border-radius:0 0 40px 0}
.card-date{margin:30px 26px 0;font-size:12px;color:var(--blue)}
.card-text{margin:14px 26px 0;font-size:13.5px;line-height:21px;color:var(--navy)}
.card-text.hover{text-decoration:underline}

/* footer */
.footer{left:0;top:4037px;width:1200px;height:417px;border-radius:150px 0 0 0;background:var(--navy);color:var(--white)}
.f-head{font-size:19px;top:92px}
.f-call{left:87px;top:138px;font-size:25px}
.f-mail{left:87px;top:168px;font-size:14px;opacity:.85}
.f-social{left:87px;top:207px;display:flex;gap:9px}
.f-social span{width:42px;height:42px;border-radius:50%;border:1.5px solid var(--sky)}
.f-social span.on{background:var(--sky)}
.f-links{top:134px;display:flex;flex-direction:column;gap:8.5px;font-size:13.5px;opacity:.9}
.f-input{left:788px;top:133px;width:324px;height:42px;border-radius:21px;background:#3a4c9e;font-size:13px;padding:0 18px;display:flex;align-items:center;opacity:.95}
.f-submit{left:788px;top:196px;width:122px;height:41px}
.f-copy{left:87px;top:356px;font-size:13px}
.f-copy span{color:var(--sky)}
</style>
</head>
<body>

<header>
  <div class="abs topbar"><span class="mail">e. info@farvintalabs.example</span><span class="call">Call. 555.014.2287</span></div>
  <div class="abs brand"><span class="brand-dot"></span><span class="brand-name">Farvinta Labs</span></div>
  <nav class="abs nav">
    <a class="active">Home</a><a>About Us</a><a>Services</a><a>Blog</a><a>Partners</a><a>Resources</a><a>Technologies</a><a>Careers</a>
  </nav>
  <a class="btn btn-navy nav-cta">Contact Us</a>
</header>

<section>
  <div class="abs hero" role="img" aria-label="Hands typing on a laptop with glowing padlocks and a network overlay"></div>
  <h1 class="abs hero-title">Improve your<br>security posture.</h1>
  <a class="btn btn-blue hero-cta">Contact Us</a>
</section>

<section>
  <h2 class="abs sect-title" style="top:853px">We can provide just the level of service<br>you need. No more. No less.</h2>
  <div class="abs services">
    <div class="svc"><div class="svc-icon" role="img" aria-label="Consultant at desk icon"></div>Consulting</div>
    <div class="svc"><div class="svc-icon" role="img" aria-label="Shield with gear icon"></div>Vulnerability Assessment</div>
    <div class="svc"><div class="svc-icon" role="img" aria-label="Shield with padlock circuit icon"></div>Information Systems<br>Security Audit</div>
    <div class="svc"><div class="svc-icon" role="img" aria-label="Checklist clipboard icon"></div>ISO Compliance</div>
    <div class="svc featured"><div class="svc-icon" role="img" aria-label="Hooded figure at laptop icon"></div>Penetration Testing</div>
    <div class="svc"><div class="svc-icon" role="img" aria-label="Trainer with audience icon"></div>Security Awareness Training</div>
    <div class="svc"><div class="svc-icon" role="img" aria-label="Connected screens with gear icon"></div>Social Engineering Test</div>
    <div class="svc"><div class="svc-icon" role="img" aria-label="Laptop with shield icon"></div>Protection Against DDoS</div>
    <div class="svc"><div class="svc-icon" role="img" aria-label="Hand trolley with boxes icon"></div>Procurement</div>
  </div>
  <div class="abs rule" style="left:0;top:1637px;width:1112px"></div>
</section>

<section>
  <h2 class="abs about-title">Escalating cyber threats demand an<br>elevated level of security.</h2>
  <div class="abs about-bar"></div>
  <div class="abs about-photo" role="img" aria-label="Laptop keyboard with padlock and security icons overlay"></div>
  <p class="abs about-kicker">About Company</p>
  <p class="abs about-lead">It is a long established fact that a reader will be distracted by the readable content of a page when looking at its layout. The point of using Lorem Ipsum</p>
  <p class="abs about-body">Making it look like readable English. Many desktop publishing packages and web page editors now use Lorem Ipsum as their default model text, and a search for 'lorem ipsum' will uncover many web sites still in their infancy ...</p>
  <a class="btn btn-blue about-cta">About Us</a>
</section>

<section>
  <div class="abs band" role="img" aria-label="Blue tinted photo of hands on a keyboard"></div>
  <h2 class="abs band-title">Ready to see how<br>cyber security services can help?</h2>
  <a class="btn btn-white band-cta">Get Started Now</a>
</section>

<section>
  <h2 class="abs sect-title" style="top:2862px">What our clients say</h2>
  <div class="abs client-photo" role="img" aria-label="Portrait of a client in a business suit"></div>
  <div class="abs quote-mark">&ldquo;&ldquo;</div>
  <p class="abs quote">It is a long established fact that a reader will be distracted by the readable content of a page when looking at its layout. The point of using Lorem Ipsum is that it has a more-or-less normal distribution of letters, as opposed to using 'Content here...</p>
  <p class="abs quote-by"><b>Marlo Penrick</b> - National Sales Manager<br>Vantrel Holdings Limited</p>
  <div class="abs dots"><span></span><span class="on"></span><span></span><span></span></div>
  <div class="abs rule" style="left:87px;top:3311px;width:1025px"></div>
</section>

<section>
  <h2 class="abs articles-title">Trending articles</h2>
  <a class="btn btn-navy articles-cta">View All</a>
  <article class="card" style="left:175px">
    <div class="card-img" role="img" aria-label="Desk with shield illustration and notebook" style="background:linear-gradient(150deg,#d9c7ae,#eef0f4)"></div>
    <p class="card-date">30 JAN 2021</p>
    <p class="card-text">It is a long established fact that a reader will be distracted by the readable.</p>
  </article>
  <article class="card" style="left:469px">
    <div class="card-img" role="img" aria-label="Hooded hacker with digital screens" style="background:linear-gradient(150deg,#2b3848,#5d7e95)"></div>
    <p class="card-date">30 JAN 2021</p>
    <p class="card-text hover">It is a long established fact that a reader will be distracted by the readable.</p>
  </article>
  <article class="card" style="left:762px">
    <div class="card-img" role="img" aria-label="Hands typing with padlock icons overlay" style="background:linear-gradient(150deg,#e6d6c8,#8b7364)"></div>
    <p class="card-date">30 JAN 2021</p>
    <p class="card-text">It is a long established fact that a reader will be distracted by the readable.</p>
  </article>
</section>

<footer class="abs footer">
  <h3 class="abs f-head" style="left:87px">Farvinta Labs</h3>
  <p class="abs f-call">Call. 800.555.0193</p>
  <p class="abs f-mail">e. info@farvintalabs.example</p>
  <div class="abs f-social"><span aria-label="Social profile one"></span><span class="on" aria-label="Social profile two"></span><span aria-label="Social profile three"></span></div>

  <h3 class="abs f-head" style="left:437px">Quick Links</h3>
  <div class="abs f-links" style="left:437px"><a>Home</a><a>About Us</a><a>Services</a><a>Blog</a><a>Partners</a><a>Resources</a><a>Technologies</a></div>
  <div class="abs f-links" style="left:564px"><a>Careers</a><a>Terms &amp; Conditions</a><a>Privacy Policy</a><a>Support</a></div>

  <h3 class="abs f-head" style="left:788px">Subscribe Us</h3>
  <div class="abs f-input">name@email.com</div>
  <a class="btn btn-blue f-submit">Submit</a>

  <p class="abs f-copy">© 2021 <span>Farvinta Labs.</span> All Rights Reserved</p>
</footer>

</body>
</html>
```